R4 Pips (CBD candy infused with Delta-8)

The proposed logo are two pool table balls. One is a D and the other is an 8, its a brand and we need a label for Gummy human treats. This treats are being infused with Delt-8. I i will upload examples only. The example is of the type of labels needed (package and label for bottle)

Target Market(s)

Your professionals

Font styles to use
Sans Serif

Requirements
Must have
• Youthful look
Nice to have
• Consider using the Delta symbol instead of the D.
Also, I provided a sample of a label that's used on two type of packages.

```html
<!DOCTYPE html>
<html lang="en">
<head>
<meta charset="utf-8">
<title>R4 Pips – Tin Lid Label</title>
<link rel="stylesheet" href="https://fonts.googleapis.com/css2?family=Archivo+Black&display=swap">
<style>
  :root {
    --bg: #ffffff;
    --lime: #bcd155;
    --lime-edge: #a9bf45;
    --purple: #6c3d8f;
    --green: #2f6b3c;
    --rim: #3fb6c2;
  }
  html, body {
    margin: 0;
    width: 1200px;
    height: 1200px;
    overflow: hidden;
    background: var(--bg);
  }
  .canvas {
    position: relative;
    width: 1200px;
    height: 1200px;
    display: flex;
    align-items: center;
    justify-content: center;
  }
  .lid-label {
    position: relative;
    width: 880px;
    height: 880px;
    background: var(--lime);
    border-radius: 90px;
    box-shadow: inset 0 0 0 10px var(--lime-edge), 0 0 0 6px var(--rim);
    font-family: "Archivo Black", sans-serif;
    color: var(--green);
    text-transform: uppercase;
  }
  .tagline {
    position: absolute;
    top: 110px;
    left: 300px;
    font-size: 30px;
    letter-spacing: 2px;
  }
  .brand {
    position: absolute;
    top: 250px;
    left: 90px;
    display: flex;
    align-items: center;
    gap: 28px;
  }
  .brand-dot {
    width: 110px;
    height: 110px;
    border-radius: 50%;
    background: var(--purple);
  }
  .brand-name {
    font-size: 150px;
    line-height: 1;
    color: var(--purple);
    text-transform: none;
  }
  .infusion {
    position: absolute;
    top: 470px;
    right: 100px;
    text-align: right;
    font-size: 40px;
    line-height: 1.05;
  }
  .net-weight {
    position: absolute;
    bottom: 110px;
    left: 110px;
  }
  .net-weight .kind { font-size: 22px; }
  .net-weight .amount { font-size: 44px; }
  .dosage {
    position: absolute;
    bottom: 90px;
    right: 110px;
  }
  .dosage .strength { font-size: 44px; }
  .dosage .per { font-size: 20px; }
  .dosage .note { font-size: 14px; text-transform: none; }
</style>
</head>
<body>
  <main class="canvas">
    <section class="lid-label">
      <p class="tagline">Premium CDB Edibles</p>
      <div class="brand">
        <span class="brand-dot"></span>
        <span class="brand-name">R4 Pips</span>
      </div>
      <p class="infusion">CBD Candy<br>Infused<br>With Delta-8</p>
      <div class="net-weight">
        <div class="kind">Dietary Supplement</div>
        <div class="amount">Net Wt 40G</div>
      </div>
      <div class="dosage">
        <div class="strength">CBD 75MG</div>
        <div class="per">Approx. per pouch</div>
        <div class="note">(approx. 2.5mg per gummy)</div>
      </div>
    </section>
  </main>
</body>
</html>
```